Blue Harbor Audio

need a business card for a dj and sound equipment hire(rentals) business based in Melbourne. i have attached a current card get an idea. card needs to be unique professional looking.

ps.this card is not for a DJ. it's a rental business of dj equipment and pa systems.

Industry/Entity Type

Business

Font styles to use
Sans Serif
Script

Requirements
Must have
• Business Name: BLUE HARBOR AUDIO
Contact Person: RAVINDU PERERA
Mobile: 047 BLAST 28
Email: RAVINDU@BLUEHARBORAUDIO.COM.AU
Website: WWW.BLUEHARBORAUDIO.COM.AU
Facebook: WWW.FACEBOOK.CM/BLUEHARBORAUDIO.COM.AU

```html
<!DOCTYPE html>
<html lang="en">
<head>
<meta charset="utf-8">
<title>Blue Harbor Audio – Business Card</title>
<link href="https://fonts.googleapis.com/css2?family=Roboto:wght@300;400;700;900&display=swap" rel="stylesheet">
<style>
  :root {
    --page-bg: #d8d3cb;
    --card-bg: #0a0a0a;
    --ink: #ffffff;
    --ink-soft: #e6e6e6;
    --grey-hi: rgba(150,150,150,.9);
    --grey-mid: rgba(70,70,70,.6);
    --violet: rgba(122,47,208,.85);
    --magenta: rgba(224,36,110,.85);
    --cyan: rgba(31,163,216,.75);
    --amber: rgba(241,194,27,.8);
  }
  html, body {
    margin: 0;
    width: 1200px;
    height: 1023px;
    overflow: hidden;
    background: var(--page-bg);
  }
  .card {
    position: absolute;
    left: 100px;
    top: 206px;
    width: 1000px;
    height: 611px;
    background: var(--card-bg);
    overflow: hidden;
    font-family: "Roboto", Arial, sans-serif;
    color: var(--ink);
    box-shadow: 0 10px 30px rgba(0,0,0,.25);
  }
  .equipment-photo,
  .pixel-mosaic {
    position: absolute;
    inset: 0;
  }
  .equipment-photo {
    background:
      radial-gradient(circle 85px at 130px 95px, var(--grey-hi), var(--grey-mid) 55%, transparent 100%),
      radial-gradient(circle 65px at 330px 405px, var(--grey-hi), var(--grey-mid) 55%, transparent 100%),
      radial-gradient(ellipse 190px 105px at 470px 355px, rgba(110,110,110,.8), rgba(40,40,40,.5) 60%, transparent 100%);
  }
  .pixel-mosaic {
    background:
      radial-gradient(ellipse 170px 95px at 880px 145px, var(--amber), transparent 100%),
      radial-gradient(ellipse 190px 110px at 760px 220px, var(--magenta), transparent 100%),
      radial-gradient(ellipse 180px 105px at 640px 295px, var(--violet), transparent 100%),
      radial-gradient(ellipse 150px 85px at 545px 380px, var(--cyan), transparent 100%);
  }
  .brand-name {
    position: absolute;
    left: 48px;
    top: 262px;
    margin: 0;
    font-size: 36px;
    font-weight: 700;
    letter-spacing: .5px;
  }
  .person-name {
    position: absolute;
    right: 44px;
    top: 36px;
    margin: 0;
    font-size: 44px;
    font-weight: 900;
    letter-spacing: 1px;
  }
  .contact-list {
    position: absolute;
    margin: 0;
    padding: 0;
    list-style: none;
    font-size: 23px;
    font-weight: 300;
    color: var(--ink-soft);
    letter-spacing: .5px;
  }
  .contact-list li {
    display: flex;
    align-items: center;
    gap: 14px;
    margin-top: 10px;
  }
  .contact-list svg { width: 22px; height: 22px; flex: none; }
  .contact-direct { left: 48px; bottom: 40px; }
  .contact-online { right: 44px; bottom: 40px; }
</style>
</head>
<body>
  <main class="card">
    <div class="equipment-photo" role="img" aria-label="Black and white photo of speakers and a DJ mixing desk"></div>
    <div class="pixel-mosaic" role="img" aria-label="Colourful pixel mosaic graphic in purple, pink, blue and yellow"></div>

    <h1 class="brand-name">Blue Harbor Audio</h1>
    <h2 class="person-name">RAVINDU PERERA</h2>

    <ul class="contact-list contact-direct">
      <li>
        <svg viewBox="0 0 24 24" aria-hidden="true"><path fill="#fff" d="M6.6 10.8a15.1 15.1 0 0 0 6.6 6.6l2.2-2.2a1 1 0 0 1 1-.25 11.4 11.4 0 0 0 3.6.57 1 1 0 0 1 1 1V20a1 1 0 0 1-1 1A17 17 0 0 1 3 4a1 1 0 0 1 1-1h3.5a1 1 0 0 1 1 1c0 1.25.2 2.45.57 3.6a1 1 0 0 1-.25 1z"/></svg>
        <span>047 BLAST 28</span>
      </li>
      <li>
        <svg viewBox="0 0 24 24" aria-hidden="true"><rect x="2" y="5" width="20" height="14" fill="#fff"/><path d="M2 5l10 8 10-8" fill="none" stroke="#0a0a0a" stroke-width="2"/></svg>
        <span>RAVINDU@BLUEHARBORAUDIO.COM.AU</span>
      </li>
    </ul>

    <ul class="contact-list contact-online">
      <li>
        <svg viewBox="0 0 24 24" aria-hidden="true"><circle cx="12" cy="12" r="10" fill="#fff"/><path d="M2 12h20M12 2c3 3 3 17 0 20M12 2c-3 3-3 17 0 20" fill="none" stroke="#0a0a0a" stroke-width="1.4"/></svg>
        <span>BLUEHARBORAUDIO.COM.AU</span>
      </li>
      <li>
        <svg viewBox="0 0 24 24" aria-hidden="true"><circle cx="12" cy="12" r="9" fill="#fff"/></svg>
        <span>/BLUEHARBORAUDIO.COM.AU</span>
      </li>
    </ul>
  </main>
</body>
</html>
```